Website Landing Page for Brightfall Systems

Create a custom designed website landing page for our business. Looking for a professional upscale design that incorporates our logo and logo colors into the theme. I want a standard fixed frame website, not a constant scrolling format that seems to be the trend. To start with I'm looking for more of the graphic design part, maybe a concept or theme, I don't expect to see a finished project. Not interested in generic templates or layouts.

The name of our company is Brightfall Systems and I've attached our logo below. I'd like to have the web page have the same look and feel of our logo, as well as the colors. Our company, Brightfall Systems does system design, installation, and programming, of residential and commercial Audio/Video and Automation systems. We do home theaters, lighting and building automation, video conferencing systems, security camera installations, conference rooms, projectors, distributed audio systems, and similar Technology projects. This will be a professional services/informational website. We will not sell products on this website. This website will be used to advertise our company and communicate our services to prospective customers. Having a well designed, professional and clean website is one way we want to distinguish our company from the competition.

Here are some examples of what I consider a professional well designed website
http://www.qorlamstudio.com/Work/

Last year we had our tradlo store designed (with PixelMarket) and I'm really happy with the way it turned out. You can see it at www.HolvenGearDepot.com I consider this to be a great design and looking for the same level of quality with this new website. However, do not copy or use any part of this design in this new project. This tradlo store is completely separate from our other company Brightfall Systems. I only mention this tradlo store an an example of good work.

Reason: Still going through designs.

Reason: Still working on project and have not had time to review all designs and request revisions.

Reason: Sill going through designs and requesting revisions

Reason: still going through all the submissions we received.

Target Market(s)

People interested in Audio/Video, home theaters, home automation. We do sales, system design, and programming. We typically work on larger projects with both residential and commercial customers.

Industry/Entity Type

Business

Number of Pages Required

1 page

Requirements
Must have
• Great design elements. Please use a white background. I think white goes well with our logo colors.

```html
<!DOCTYPE html>
<html lang="en">
<head>
<meta charset="utf-8">
<title>Brightfall Systems</title>
<link href="https://fonts.googleapis.com/css2?family=Open+Sans:wght@400;600;700&family=Roboto:wght@400;500&display=swap" rel="stylesheet">
<style>
:root{
  --green:#8cc63f;
  --green-dark:#5f9a25;
  --blue:#29a9e0;
  --blue-dark:#1b8fc6;
  --ink:#1b1b1b;
  --text:#666;
  --white:#fff;
  --card:#f1f1f1;
  --footer:#141414;
}
*{margin:0;padding:0;box-sizing:border-box}
html,body{width:1200px;height:3468px;overflow:hidden}
body{position:relative;background:var(--white);font-family:"Open Sans",Arial,sans-serif;color:var(--text)}
.abs{position:absolute}
.photo{position:absolute}
/* nav */
.topbar{position:absolute;left:0;top:0;width:1200px;height:110px;z-index:5}
.nav a{position:absolute;top:34px;color:var(--white);font-size:16px;text-decoration:none;font-family:"Open Sans",sans-serif}
.nav a.active{border-bottom:3px solid var(--green);padding-bottom:10px}
.brand{position:absolute;display:flex;align-items:center;gap:12px}
.brand .dot{width:62px;height:62px;border-radius:50%;border:5px solid var(--green);background:var(--white)}
.brand .name{font-family:"Roboto",sans-serif;font-weight:500;color:var(--green);font-size:24px;line-height:1.05;width:160px}
/* hero */
.hero{left:0;top:0;width:1200px;height:700px;background:linear-gradient(180deg,#7d8e9e 0%,#5d6d7a 35%,#3f5a3a 60%,#3e6a2e 100%)}
.hero h1{position:absolute;top:280px;width:1200px;text-align:center;color:var(--white);font-family:"Open Sans",sans-serif;font-weight:400;font-size:58px}
.hero p{position:absolute;top:356px;left:220px;width:760px;text-align:center;color:var(--white);font-size:22px;line-height:1.3}
.btn{position:absolute;display:inline-block;color:var(--white);font-size:17px;border-radius:28px;text-align:center;line-height:52px;height:52px;box-shadow:0 3px 0 rgba(0,0,0,.25)}
.btn.blue{background:var(--blue)}
.btn.green{background:var(--green)}
.dots{position:absolute;top:582px;left:542px;display:flex;gap:10px}
.dots span{width:20px;height:20px;border-radius:50%;background:var(--white)}
.dots span:first-child{background:var(--green)}
/* welcome */
.welcome{left:0;top:640px;width:1200px;height:370px;background:linear-gradient(180deg,#8cc63f 0%,#7bb63a 100%)}
.mark{position:absolute;width:64px;height:64px;border-radius:50%;background:var(--white);border:6px solid var(--blue)}
h2{font-family:"Roboto",sans-serif;font-weight:400}
.welcome h2{position:absolute;top:72px;width:1200px;text-align:center;color:var(--ink);font-size:42px}
.welcome p{position:absolute;top:140px;left:110px;width:980px;text-align:center;color:var(--white);font-size:15px;line-height:1.65}
/* about */
.video{left:79px;top:1066px;width:400px;height:260px;border:5px solid #cfcfcf;background:linear-gradient(135deg,#2c2a28,#6b5640 55,#1f1d1c);background:linear-gradient(135deg,#2c2a28 0%,#6b5640 55%,#1f1d1c 100%)}
.video .vt{position:absolute;left:12px;top:8px;color:var(--white);font-size:20px}
.video .play{position:absolute;left:168px;top:102px;width:62px;height:44px;border-radius:10px;background:#d9261c}
.about h2{position:absolute;left:534px;top:1058px;color:var(--blue);font-size:40px}
.about p{position:absolute;left:534px;top:1126px;width:590px;font-size:15.5px;line-height:1.72}
/* services */
.services{left:0;top:1340px;width:1200px;height:500px}
.services h2{position:absolute;left:474px;top:128px;color:var(--ink);font-size:36px;font-weight:500}
.services p{position:absolute;left:578px;top:190px;width:420px;color:var(--white);font-size:15.5px;line-height:1.7}
.vline{position:absolute;width:2px;background:rgba(255,255,255,.7)}
/* projects */
.projects h2{position:absolute;top:1882px;width:1200px;text-align:center;color:var(--blue);font-size:40px}
.card{position:absolute;top:1979px;width:234px;height:281px;background:var(--card);text-align:center}
.card .img{height:140px}
.card h3{margin-top:14px;font-family:"Roboto",sans-serif;font-weight:400;color:var(--blue);font-size:22px}
.card p{margin:8px 14px 0;font-size:15px;line-height:1.55}
.card .more{margin-top:4px;font-size:14px;color:var(--blue)}
/* gallery */
.gallery{left:0;top:2270px;width:1200px;height:930px}
.gallery h2{position:absolute;top:130px;width:1200px;text-align:center;color:var(--ink);font-size:40px}
/* footer */
.footer{left:0;top:3160px;width:1200px;height:260px}
.flinks{position:absolute;top:3313px;width:1200px;text-align:center;font-size:16px;color:var(--white)}
.flinks span{padding:0 18px;border-left:1px solid var(--white)}
.flinks span:first-child{border-left:0}
.social{position:absolute;top:3357px;left:478px;display:flex;gap:14px}
.social span{width:36px;height:36px;border-radius:50%;border:2px solid var(--white);background:rgba(255,255,255,.15)}
.copy{position:absolute;left:0;top:3417px;width:1200px;height:51px;background:var(--blue);color:var(--white);text-align:center;line-height:51px;font-size:15px}
</style>
</head>
<body>

<!-- hero -->
<div class="photo hero" role="img" aria-label="City skyline with high-rise buildings behind a leafy park and pond">
  <h1>Brightfall Systems</h1>
  <p>We are a leader in the system design, installation, and programming of residential and commercial Audio/Video and Automation systems.</p>
  <span class="btn blue" style="left:497px;top:427px;width:200px;font-weight:600;font-size:16px">CONTACT US NOW</span>
  <div class="dots"><span></span><span></span><span></span><span></span></div>
</div>

<!-- top bar -->
<svg class="topbar" viewBox="0 0 1200 110" aria-hidden="true">
  <path d="M0 0H1200V70C900 68 800 82 600 92 400 80 250 70 0 74Z" fill="#2a2a2a" opacity=".92"/>
  <path d="M0 74C250 70 400 80 600 92 800 82 900 68 1200 70V84C900 80 800 96 600 106 400 94 250 84 0 86Z" fill="#29a9e0"/>
</svg>
<nav class="nav" style="position:absolute;top:0;left:0;width:1200px;z-index:6">
  <a class="active" style="left:79px">HOME</a>
  <a style="left:190px">ABOUT US</a>
  <a style="left:331px">SERVICES</a>
  <a style="left:784px">PROJECTS</a>
  <a style="left:907px">GALLERY</a>
  <a style="left:1020px">CONTACT US</a>
  <div class="brand" style="left:462px;top:12px"><span class="dot"></span><span class="name">Brightfall Systems</span></div>
</nav>

<!-- welcome -->
<section class="abs welcome">
  <svg class="abs" style="left:0;top:-40px" width="1200" height="80" viewBox="0 0 1200 80" aria-hidden="true">
    <path d="M0 50C300 0 500 10 700 40 900 70 1050 30 1200 20V80H0Z" fill="#29a9e0" opacity=".8"/>
    <path d="M0 60C300 20 500 30 700 55 900 80 1050 45 1200 35V80H0Z" fill="#8cc63f"/>
  </svg>
  <span class="mark" style="left:568px;top:8px;border-color:var(--green)"></span>
  <h2>Welcome To Brightfall Systems</h2>
  <p>Lorem Ipsum is simply dummy text of the printing and typesetting industry. Lorem Ipsum has been the industry's standard dummy text ever since the 1500s, when an unknown printer took a galley of type and scrambled it to make a type specimen book. It has survived not only five centuries, but also the leap into electronic typesetting, remaining essentially unchanged. It was popularised in the 1960s with the release of Letraset sheets containing Lorem Ipsum passages...</p>
  <span class="btn blue" style="left:512px;top:268px;width:176px">READ MORE &#187;</span>
</section>

<!-- about -->
<section class="about">
  <div class="photo video" role="img" aria-label="Video still of a modern lounge bar with stools and warm lighting">
    <span class="vt">Title</span>
    <span class="play"></span>
    <svg class="abs" style="left:188px;top:114px" width="22" height="20" aria-hidden="true"><path d="M2 0L20 10 2 20Z" fill="#fff"/></svg>
  </div>
  <h2>About Us</h2>
  <p>Lorem Ipsum is simply dummy text of the printing and typesetting industry. Lorem Ipsum has been the industry's standard dummy text ever since the 1500s, when an unknown printer took a galley of type and scrambled it to make a type specimen book. It has survived not only five centuries, but also the leap into electronic typesetting, remaining essentially unchanged. It was popularised in...</p>
  <span class="btn blue" style="left:534px;top:1277px;width:170px">READ MORE &#187;</span>
</section>

<!-- services -->
<section class="abs services">
  <svg class="abs" style="left:0;top:0" width="1200" height="500" viewBox="0 0 1200 500" aria-hidden="true">
    <defs><linearGradient id="svcBg" x1="0" y1="0" x2="0" y2="1"><stop offset="0" stop-color="#3fb3e6"/><stop offset="1" stop-color="#1f94cc"/></linearGradient></defs>
    <path d="M0 20C250 -5 450 5 600 40 800 5 1000 -5 1200 20V500H0Z" fill="url(#svcBg)"/>
  </svg>
  <span class="mark" style="left:568px;top:28px;border-color:var(--green)"></span>
  <span class="vline" style="left:171px;top:125px;height:340px"></span>
  <svg class="abs" style="left:171px;top:140px" width="14" height="20" aria-hidden="true"><path d="M2 0L12 10 2 20Z" fill="#fff"/></svg>
  <span class="vline" style="left:1029px;top:125px;height:340px"></span>
  <!-- left icons -->
  <svg class="abs" style="left:76px;top:130px" width="80" height="340" viewBox="0 0 80 340" fill="none" stroke="#fff" stroke-width="4" aria-hidden="true">
    <rect x="14" y="6" width="46" height="32" fill="#1a1a1a"/><path d="M28 46H46M37 38V46"/>
    <path d="M10 132L37 108 64 132M18 126V158H56V126"/><rect x="31" y="138" width="12" height="20"/>
    <rect x="12" y="205" width="50" height="34"/><circle cx="26" cy="222" r="5"/><circle cx="48" cy="222" r="5"/>
    <path d="M8 300L52 284 58 298 14 314ZM20 312L16 330"/>
  </svg>
  <div class="photo" style="left:204px;top:190px;width:333px;height:267px;background:linear-gradient(160deg,#3a3a3a,#0d0d0d);border-radius:6px" role="img" aria-label="Black home theater speaker set with subwoofer and receiver"></div>
  <h2>Home Theaters</h2>
  <p>Lorem Ipsum is simply dummy text of the printing and typesetting industry. Lorem Ipsum has been the industry's standard dummy text ever since the 1500s, when an unknown printer took a galley of type and scrambled it to make a type specimen book. It has survived not only five centuries, but also the leap into electronic typesetting, remaining essentially unchanged...</p>
  <span class="btn green" style="left:575px;top:392px;width:172px">READ MORE &#187;</span>
  <!-- right icons -->
  <svg class="abs" style="left:1050px;top:130px" width="80" height="340" viewBox="0 0 80 340" fill="none" stroke="#fff" stroke-width="4" aria-hidden="true">
    <rect x="10" y="14" width="54" height="28" rx="6"/><circle cx="37" cy="28" r="7"/><path d="M22 42L16 52M52 42L58 52"/>
    <rect x="10" y="104" width="56" height="26" rx="13"/><circle cx="50" cy="117" r="7"/>
    <rect x="14" y="190" width="46" height="46" rx="6"/><circle cx="28" cy="204" r="5"/><circle cx="46" cy="222" r="5"/>
    <circle cx="37" cy="300" r="20"/><path d="M31 290L47 300 31 310Z" fill="#fff"/>
  </svg>
</section>

<!-- projects -->
<section class="projects">
  <h2>Our Projects</h2>
  <div class="card" style="left:79px"><div class="photo img" style="position:relative;background:linear-gradient(180deg,#1d3f8a,#c08a3c)" role="img" aria-label="Luxury home exterior at dusk with palm trees"></div><h3>Project Name</h3><p>Lorem Ipsum is simply dummy text of the printing type...</p><div class="more">READ MORE &#187;</div></div>
  <div class="card" style="left:349px"><div class="photo img" style="position:relative;background:linear-gradient(180deg,#6a5a48,#c9b89b)" role="img" aria-label="Living room with large wall-mounted screen and sofa"></div><h3>Project Name</h3><p>Lorem Ipsum is simply dummy text of the printing type...</p><div class="more">READ MORE &#187;</div></div>
  <div class="card" style="left:620px"><div class="photo img" style="position:relative;background:linear-gradient(180deg,#4a3a30,#8a8a8a)" role="img" aria-label="Conference room with long table and display screen"></div><h3>Project Name</h3><p>Lorem Ipsum is simply dummy text of the printing type...</p><div class="more">READ MORE &#187;</div></div>
  <div class="card" style="left:890px"><div class="photo img" style="position:relative;background:linear-gradient(180deg,#d8d4cc,#8f8576)" role="img" aria-label="Bright lounge with media wall and seating"></div><h3>Project Name</h3><p>Lorem Ipsum is simply dummy text of the printing type...</p><div class="more">READ MORE &#187;</div></div>
</section>

<!-- gallery -->
<section class="abs gallery">
  <svg class="abs" style="left:0;top:0" width="1200" height="930" viewBox="0 0 1200 930" aria-hidden="true">
    <defs><linearGradient id="galBg" x1="0" y1="0" x2="0" y2="1"><stop offset="0" stop-color="#8cc63f"/><stop offset="1" stop-color="#6fae2c"/></linearGradient></defs>
    <path d="M0 10C250 40 450 60 600 60 800 55 1000 35 1200 5V930H0Z" fill="url(#galBg)"/>
  </svg>
  <span class="mark" style="left:568px;top:40px"></span>
  <h2>Gallery</h2>
</section>
<div class="photo" style="left:79px;top:2504px;width:520px;height:290px;background:linear-gradient(135deg,#7a1a18,#2a1a16)" role="img" aria-label="Red media room with lounge chair and floor speakers"></div>
<svg class="abs" style="left:324px;top:2634px" width="30" height="30" aria-hidden="true"><path d="M15 0V30M0 15H30" stroke="#fff" stroke-width="3"/></svg>
<div class="photo" style="left:610px;top:2504px;width:250px;height:290px;background:linear-gradient(180deg,#e6e6e6,#4a4a4a)" role="img" aria-label="Television on a console with center speaker against a white brick wall"></div>
<div class="photo" style="left:872px;top:2504px;width:249px;height:290px;background:linear-gradient(180deg,#1a2030,#8a6a2a)" role="img" aria-label="Illuminated house garden at night"></div>
<div class="photo" style="left:79px;top:2808px;width:250px;height:290px;background:linear-gradient(180deg,#e0e0e0,#7a4a2a)" role="img" aria-label="Office reception with wood panel wall and screens"></div>
<div class="photo" style="left:340px;top:2808px;width:249px;height:290px;background:linear-gradient(180deg,#b05a2a,#3a2418)" role="img" aria-label="Wood paneled room with television and speakers"></div>
<div class="photo" style="left:601px;top:2808px;width:520px;height:290px;background:linear-gradient(135deg,#1a3a7a,#0a1a40)" role="img" aria-label="Cinema with rows of seats and blue step lighting"></div>

<!-- footer -->
<section class="abs footer">
  <svg class="abs" style="left:0;top:0" width="1200" height="260" viewBox="0 0 1200 260" aria-hidden="true">
    <path d="M0 20C300 60 500 70 600 70 800 70 950 55 1200 25V260H0Z" fill="#4c7d20"/>
    <path d="M0 36C300 76 500 86 600 86 800 86 950 70 1200 40V260H0Z" fill="#141414"/>
  </svg>
  <div class="brand" style="left:462px;top:56px"><span class="dot" style="border-color:var(--blue)"></span><span class="name">Brightfall Systems</span></div>
</section>
<div class="flinks"><span>Home</span><span>About Us</span><span>Services</span><span>Projects</span><span>Gallery</span><span>Contact Us</span></div>
<div class="social"><span></span><span></span><span></span><span></span><span></span></div>
<div class="copy">&copy; <strong>Brightfall Systems</strong> -2017. All Rights Reserved.</div>

</body>
</html>
```